Aviation Law Firm Needs Envelope Design

The envelope design must be EYE CATCHING and sexy, yet very professional. The information in the return address should be in the upper left hand corner and read:
The Varrow Law Firm
P.O. Box 5817
Cedar Vale, Ohio 33214

The word: "ADVERTISEMENT" must appear on the front of the envelope in some fashion.

The colors should compliment the letterhead image (attached). However, I would like for the envelope to remain white or light colored in the upper right hand corner so that the post office can read any stamps, etc.

Target Market(s)

Pilots; Legal Clients

Industry/Entity Type

Law Firm

Font styles to use
Serif
Sans Serif

Colors
191919
fbee3e
ffffff

Requirements
Must have
• Must capture the use of the entire envelope, BUT leave space for receiver's address and post office stamps, etc.

```html
<!DOCTYPE html>
<html lang="en">
<head>
<meta charset="utf-8">
<title>The Varrow Law Firm – Envelope</title>
<link rel="stylesheet" href="https://fonts.googleapis.com/css2?family=Arimo:wght@400;700&display=swap">
<style>
  :root {
    --ink: #191919;
    --sun: #fbee3e;
    --paper: #ffffff;
    --backdrop: #e9e9ea;
    --faint-sun: #f7f1c4;
  }
  * { margin: 0; padding: 0; box-sizing: border-box; }
  html, body { width: 1200px; height: 800px; overflow: hidden; }
  body {
    background: var(--backdrop);
    font-family: "Arimo", Arial, sans-serif;
    color: var(--ink);
    position: relative;
  }
  .envelope {
    position: absolute;
    width: 760px;
    height: 330px;
    background: var(--paper);
    box-shadow: 0 4px 14px rgba(0,0,0,0.12);
    overflow: hidden;
  }
  .envelope--back { left: 150px; top: 30px; }
  .envelope--front { left: 330px; top: 440px; }

  .flap-band { position: absolute; left: 0; top: 0; width: 760px; height: 70px; }
  .flap-name {
    position: absolute; left: 0; top: 22px; width: 700px;
    text-align: center;
    font-size: 20px; font-weight: 400; letter-spacing: 3px;
  }
  .flap-mark {
    position: absolute; left: 0; top: 130px; width: 760px;
    text-align: center;
    font-size: 60px; font-weight: 700; letter-spacing: 2px;
    color: var(--faint-sun);
  }

  .return-address {
    position: absolute; left: 26px; top: 24px;
    font-size: 15px; font-weight: 700; letter-spacing: 2.4px; line-height: 1.35;
    font-style: normal;
  }
  .brand {
    position: absolute; left: 26px; top: 166px;
    display: flex; align-items: center; gap: 8px;
  }
  .brand__dot { width: 22px; height: 22px; border-radius: 50%; background: var(--sun); }
  .brand__name { font-size: 18px; font-weight: 700; letter-spacing: 1px; }

  .wave { position: absolute; left: 0; top: 0; width: 760px; height: 330px; }
  .advert-label {
    position: absolute; right: 28px; bottom: 14px;
    font-size: 26px; font-weight: 700; letter-spacing: 6px;
  }
</style>
</head>
<body>
  <section class="envelope envelope--back" aria-label="Envelope back">
    <svg class="flap-band" viewBox="0 0 760 70" aria-hidden="true">
      <polygon points="0,0 760,0 760,22 700,70 0,70" fill="var(--sun)"/>
    </svg>
    <div class="flap-name">The Varrow Law Firm</div>
    <div class="flap-mark">Varrow</div>
  </section>

  <section class="envelope envelope--front" aria-label="Envelope front">
    <svg class="wave" viewBox="0 0 760 330" aria-hidden="true">
      <path d="M0,212 C220,272 520,262 760,268 L760,330 L0,330 Z" fill="var(--sun)"/>
      <path d="M0,212 C220,272 520,262 760,268" fill="none" stroke="var(--ink)" stroke-width="5"/>
    </svg>
    <address class="return-address">
      The Varrow Law Firm<br>
      P.O. Box 5817<br>
      Cedar Vale, Ohio 33214
    </address>
    <div class="brand">
      <span class="brand__dot"></span>
      <span class="brand__name">Varrow</span>
    </div>
    <div class="advert-label">ADVERTISEMENT</div>
  </section>
</body>
</html>
```